Lumo Quest - Main Menu - Re-Design

I want to have a refresh for this app's main menu. There are some different items on the menu depending on the language (English vs. Non-English) and version (Pro vs. Free). I have attached screenshots of the different conditions. This app is a collection of brain training games.

Need designs for light and dark mode. Need designs for both portrait and landscape mode.

Here is a link to the app in Vexo Shelf.
https://shelf.vexomarket.test/store/apps/details?id=tarnwick.lumoquest

Here is a link to the app in the Quorra App Depot.
https://apps.quorradepot.test/us/app/lumo-quest-brain-training/id573918204?ls=1&mt=8

```html
<!DOCTYPE html>
<html lang="en">
<head>
<meta charset="utf-8">
<title>Lumo Quest Pro – Main Menu Re-Design</title>
<link href="https://fonts.googleapis.com/css2?family=Rubik:wght@700;800;900&family=Roboto:wght@300;400&display=swap" rel="stylesheet">
<style>
:root{
  --board:#9fd3d2;
  --ink:#0f1530;
  --dark:#0c0b14;
  --dark-land:#15101f;
  --light:#f4f4f7;
  --blue-a:#1f6fd6;--blue-b:#45a8f2;
  --violet-a:#8a48de;--violet-b:#d75ee6;
  --pink:#e65ce0;
  --info:#3b8ee8;
  --teal-card:#9dd3d0;
  --tag-blue:#2456c9;
  --green:#6bb43a;--sea:#1e8c8c;--navy:#1f5ea6;--rose:#d457c8;--amber:#eea11d;--steel:#9aa0ab;
}
*{box-sizing:border-box;margin:0;padding:0}
html,body{width:1200px;height:2401px;overflow:hidden}
body{background:var(--board);position:relative;font-family:"Roboto",sans-serif}
.screen{position:absolute;overflow:hidden}
.screen.dark{background:var(--dark);color:#fff}
.screen.light{background:var(--light);color:#222}
.screen.land{background:var(--dark-land);color:#fff}

/* header */
.bar{position:absolute;left:0;right:0;top:0;height:64px;display:flex;align-items:center;justify-content:space-between;padding:0 14px;font-weight:300;font-size:17px}
.dot{width:24px;height:24px;border-radius:50%;background:var(--pink);position:relative}
.dot::after{content:"";position:absolute;inset:8px;border-radius:50%;background:#fff}
.dot.info{background:var(--info)}

/* tiles */
.tile{border-radius:10px;display:flex;flex-direction:column;align-items:center;justify-content:center;color:#fff;font-family:"Rubik",sans-serif;font-weight:900;text-align:center;letter-spacing:-.2px;text-shadow:0 1px 2px rgba(0,0,0,.25)}
.tile.blue{background:linear-gradient(135deg,var(--blue-a),var(--blue-b) 60%,var(--blue-a))}
.tile.violet{background:linear-gradient(135deg,var(--violet-b),var(--violet-a) 55%,var(--violet-b))}
.ico{display:block;border-radius:50%;background:#fff;border:3px solid rgba(255,255,255,.6);position:relative}
.ico::after{content:"";position:absolute;inset:18%;border-radius:50%;background:radial-gradient(circle at 40% 35%,#ffd54a,#f39a2c 55%,#7b4fd6)}
.grid{position:absolute;display:grid;gap:10px}
.grid.portrait{left:8px;right:8px;grid-template-columns:1fr 1fr}
.grid.portrait .tile{height:154px;font-size:12.5px;gap:12px}
.grid.portrait .ico{width:78px;height:78px}

/* list menu */
.big{height:130px;font-size:12.5px;gap:10px}
.big .ico{width:72px;height:72px}
.pill{height:53px;border-radius:9px;display:flex;align-items:center;gap:4px;padding:0 6px;color:#fff;font-family:"Rubik",sans-serif;font-weight:900;font-size:12px;letter-spacing:-.3px;white-space:nowrap}
.pill .ico{width:38px;height:38px;border-width:2px;flex:none}
.pill span.t{flex:1;text-align:center}
.green{background:var(--green)}.sea{background:var(--sea)}.navy{background:var(--navy)}.rose{background:var(--rose)}.amber{background:var(--amber)}.steel{background:var(--steel)}

.demo{border-radius:6px;display:flex;height:107px;overflow:hidden}
.demo.teal{background:var(--teal-card)}
.demo.white{background:#fff;border:1px solid #ddd}
.demo .art{width:126px;flex:none}
.art.head{background:radial-gradient(circle at 50% 55%,#f1b08b,#d77a6a 35%,#9dd3d0 70%)}
.art.pieces{background:radial-gradient(ellipse at 50% 50%,#f0c23a,#e2493f 30%,#3b9f5a 50%,#f4f4f4 72%)}
.demo .txt{padding:9px 6px 0 4px;color:#fff;font-size:12px;line-height:13px}
.demo.white .txt{color:#222}
.demo h4{font-family:"Rubik",sans-serif;font-weight:900;font-size:13px;color:#fff;margin-bottom:3px}
.demo.white h4{color:#111}
.demo .src{font-size:12.5px;margin-bottom:3px}
.btn{display:inline-block;background:var(--pink);color:#fff;border-radius:14px;font-size:9px;font-weight:400;padding:6px 14px;margin-top:6px;letter-spacing:.2px;white-space:nowrap}

/* landscape */
.lgrid{position:absolute;display:grid;gap:8px}
.lgrid .tile{font-size:6.5px;gap:5px;border-radius:9px}
.wide{position:absolute;left:14px;right:14px;background:var(--teal-card);border-radius:5px;display:flex;align-items:center;color:#222;font-size:11.5px;line-height:13px}
.wide h4{font-family:"Rubik",sans-serif;font-weight:900;font-size:13px;color:#222;white-space:nowrap}
</style>
</head>
<body>

<!-- Splash, light -->
<section class="screen light" style="left:93px;top:84px;width:291px;height:632px;background:#fff">
  <div role="img" aria-label="Glossy yellow and red 3D brain, top" style="position:absolute;left:0;right:0;top:0;height:132px;background:radial-gradient(ellipse 80% 100% at 50% 0,#f5d21e,#f0b40e 45%,#e5352a 70%,#fff 71%)"></div>
  <div style="position:absolute;left:0;right:0;top:195px;text-align:center">
    <div style="width:108px;height:108px;border-radius:50%;background:var(--tag-blue);margin:0 auto 18px"></div>
    <div style="font-family:Rubik,sans-serif;font-weight:900;font-size:34px;line-height:38px;color:var(--ink)">LUMO<br>QUEST PRO</div>
    <div style="font-size:22px;font-weight:300;color:var(--tag-blue);margin-top:10px">Exercise Your Brain</div>
  </div>
  <div role="img" aria-label="Glossy yellow and red 3D brain, bottom" style="position:absolute;left:0;right:0;bottom:0;height:126px;background:radial-gradient(ellipse 80% 100% at 50% 100%,#f5d21e,#f0b40e 45%,#e5352a 70%,#fff 71%)"></div>
</section>

<!-- Splash, dark -->
<section class="screen dark" style="left:453px;top:82px;width:290px;height:628px;border-radius:26px">
  <div style="position:absolute;left:0;right:0;top:28px;text-align:center">
    <div style="width:104px;height:104px;border-radius:50%;background:var(--tag-blue);margin:0 auto 20px"></div>
    <div style="font-family:Rubik,sans-serif;font-weight:900;font-size:33px;line-height:38px">LUMO<br>QUEST PRO</div>
    <div style="font-size:22px;font-weight:300;margin-top:12px">Exercise Your Brain</div>
  </div>
  <div role="img" aria-label="Neon circuit brain beside a figure wearing a VR headset" style="position:absolute;left:0;right:0;bottom:0;height:340px;background:radial-gradient(circle at 28% 30%,rgba(230,80,220,.55),transparent 30%),radial-gradient(circle at 45% 30%,rgba(60,150,255,.55),transparent 30%),radial-gradient(ellipse at 80% 75%,rgba(40,140,255,.5),transparent 55%),var(--dark)"></div>
</section>

<!-- Grid menu, dark -->
<section class="screen dark" style="left:815px;top:84px;width:292px;height:632px">
  <div class="bar"><span class="dot"></span>Welcome Guest<span class="dot"></span></div>
  <div class="grid portrait" style="top:98px">
    <div class="tile blue"><span class="ico" role="img" aria-label="Puzzle head icon"></span>TRAINING CENTER</div>
    <div class="tile violet"><span class="ico" role="img" aria-label="Game controller icon"></span>GAMES LIST</div>
    <div class="tile violet"><span class="ico" role="img" aria-label="Head with gears icon"></span>LEARNING</div>
    <div class="tile blue"><span class="ico" role="img" aria-label="Brain icon"></span>ABOUT</div>
    <div class="tile blue"><span class="ico" role="img" aria-label="Calendar and clock icon"></span>SCHEDULE</div>
    <div class="tile violet"><span class="ico" role="img" aria-label="Stars scoreboard icon"></span>SCORES</div>
  </div>
</section>

<!-- Grid menu, light -->
<section class="screen light" style="left:93px;top:766px;width:291px;height:632px">
  <div class="bar" style="color:#222"><span class="dot"></span>Welcome Guest<span class="dot"></span></div>
  <div class="grid portrait" style="top:98px">
    <div class="tile blue"><span class="ico" role="img" aria-label="Puzzle head icon"></span>TRAINING CENTER</div>
    <div class="tile violet"><span class="ico" role="img" aria-label="Game controller icon"></span>GAMES LIST</div>
    <div class="tile violet"><span class="ico" role="img" aria-label="Head with gears icon"></span>LEARNING</div>
    <div class="tile blue"><span class="ico" role="img" aria-label="Brain icon"></span>ABOUT</div>
    <div class="tile blue"><span class="ico" role="img" aria-label="Calendar and clock icon"></span>SCHEDULE</div>
    <div class="tile violet"><span class="ico" role="img" aria-label="Stars scoreboard icon"></span>SCORES</div>
  </div>
</section>

<!-- List menu, dark -->
<section class="screen dark" style="left:455px;top:766px;width:291px;height:632px">
  <div class="bar"><span class="dot"></span>Welcome Guest<span class="dot"></span></div>
  <div style="position:absolute;left:8px;right:8px;top:68px;display:flex;flex-direction:column;gap:10px">
    <div style="display:grid;grid-template-columns:1fr 1fr;gap:10px">
      <div class="tile violet big"><span class="ico" role="img" aria-label="Game controller icon"></span>GAMES LIST</div>
      <div class="tile blue big"><span class="ico" role="img" aria-label="Puzzle head icon"></span>TRAINING CENTER</div>
    </div>
    <div class="demo teal"><div class="art head" role="img" aria-label="Illustrated head with brain, gears and light bulbs"></div><div class="txt"><h4>WATCH DEMO</h4><div class="src">Norvel Brightline</div>Sed ut perspiciatis unde omnis iste natus error sit<br><span class="btn">LEARN MORE</span></div></div>
    <div style="display:grid;grid-template-columns:1fr 1fr;gap:9px 10px">
      <div class="pill green"><span class="ico" role="img" aria-label="Upgrade arrow icon"></span><span class="t">UPGRADE</span></div>
      <div class="pill sea"><span class="ico" role="img" aria-label="Phone apps icon"></span><span class="t">MORE APPS</span></div>
      <div class="pill navy"><span class="ico" role="img" aria-label="Head with gears icon"></span><span class="t">LEARNING</span></div>
      <div class="pill rose"><span class="ico" role="img" aria-label="Stars scoreboard icon"></span><span class="t">SCORES</span></div>
      <div class="pill amber"><span class="ico" role="img" aria-label="Calendar icon"></span><span class="t">SCHEDULE</span></div>
      <div class="pill steel"><span class="ico" role="img" aria-label="Settings head icon"></span><span class="t">SETTINGS</span></div>
    </div>
    <div class="demo white"><div class="art pieces" role="img" aria-label="Colourful 3D puzzle blocks forming a brain"></div><div class="txt"><h4>WATCH DEMO</h4><div class="src">Norvel Brightline</div>Sed ut perspiciatis unde omnis iste natus error sit<br><span class="btn">LEARN MORE</span></div></div>
  </div>
</section>

<!-- List menu, light -->
<section class="screen light" style="left:815px;top:766px;width:292px;height:632px">
  <div class="bar" style="color:#222"><span class="dot"></span>Welcome Guest<span class="dot"></span></div>
  <div style="position:absolute;left:8px;right:8px;top:68px;display:flex;flex-direction:column;gap:10px">
    <div style="display:grid;grid-template-columns:1fr 1fr;gap:10px">
      <div class="tile violet big"><span class="ico" role="img" aria-label="Game controller icon"></span>GAMES LIST</div>
      <div class="tile blue big"><span class="ico" role="img" aria-label="Puzzle head icon"></span>TRAINING CENTER</div>
    </div>
    <div class="demo teal"><div class="art head" role="img" aria-label="Illustrated head with brain, gears and light bulbs"></div><div class="txt"><h4>WATCH DEMO</h4><div class="src">Norvel Brightline</div>Sed ut perspiciatis unde omnis iste natus error sit<br><span class="btn">LEARN MORE</span></div></div>
    <div style="display:grid;grid-template-columns:1fr 1fr;gap:9px 10px">
      <div class="pill green"><span class="ico" role="img" aria-label="Upgrade arrow icon"></span><span class="t">UPGRADE</span></div>
      <div class="pill sea"><span class="ico" role="img" aria-label="Phone apps icon"></span><span class="t">MORE APPS</span></div>
      <div class="pill navy"><span class="ico" role="img" aria-label="Head with gears icon"></span><span class="t">LEARNING</span></div>
      <div class="pill rose"><span class="ico" role="img" aria-label="Stars scoreboard icon"></span><span class="t">SCORES</span></div>
      <div class="pill amber"><span class="ico" role="img" aria-label="Calendar icon"></span><span class="t">SCHEDULE</span></div>
      <div class="pill steel"><span class="ico" role="img" aria-label="Settings head icon"></span><span class="t">SETTINGS</span></div>
    </div>
    <div class="demo white"><div class="art pieces" role="img" aria-label="Colourful 3D puzzle blocks forming a brain"></div><div class="txt"><h4>WATCH DEMO</h4><div class="src">Norvel Brightline</div>Sed ut perspiciatis unde omnis iste natus error sit<br><span class="btn">LEARN MORE</span></div></div>
  </div>
</section>

<!-- Landscape, Pro English -->
<section class="screen land" style="left:299px;top:1454px;width:603px;height:267px">
  <div class="bar" style="height:50px"><span class="dot info"></span>Welcome Guest<span class="dot"></span></div>
  <div class="lgrid" style="left:131px;top:51px;grid-template-columns:repeat(4,80px);grid-auto-rows:72px">
    <div class="tile blue"><span class="ico" role="img" aria-label="Puzzle head icon" style="width:44px;height:44px"></span>TRAINING CENTER</div>
    <div class="tile violet"><span class="ico" role="img" aria-label="Game controller icon" style="width:44px;height:44px"></span>GAMES LIST</div>
    <div class="tile blue"><span class="ico" role="img" aria-label="Head with gears icon" style="width:44px;height:44px"></span>LEARNING</div>
    <div class="tile violet"><span class="ico" role="img" aria-label="Upgrade arrow icon" style="width:44px;height:44px"></span>UPGRADE</div>
    <div class="tile blue"><span class="ico" role="img" aria-label="Settings head icon" style="width:44px;height:44px"></span>SETTINGS</div>
    <div class="tile violet"><span class="ico" role="img" aria-label="Calendar icon" style="width:44px;height:44px"></span>SCHEDULE</div>
    <div class="tile blue"><span class="ico" role="img" aria-label="Phone apps icon" style="width:44px;height:44px"></span>MORE APPS</div>
    <div class="tile violet"><span class="ico" role="img" aria-label="Stars scoreboard icon" style="width:44px;height:44px"></span>SCORES</div>
  </div>
  <div class="wide" style="top:215px;height:44px;padding:0 16px;gap:18px">
    <h4>WATCH DEMO</h4><div style="flex:1">Sed ut perspiciatis unde omnis iste natus error sit voluem accusantium doloremque laudantium, totam rem</div><span class="btn" style="margin:0">LEARN MORE</span>
  </div>
</section>

<!-- Landscape, Free English -->
<section class="screen land" style="left:299px;top:1750px;width:603px;height:268px">
  <div class="bar" style="height:66px;align-items:flex-start;padding-top:20px;font-size:18px"><span style="display:flex;gap:12px;align-items:center"><span class="dot"></span>Welcome</span><span style="display:flex;gap:12px;align-items:center">Guest<span class="dot"></span></span></div>
  <div class="lgrid" style="left:160px;top:26px;grid-template-columns:repeat(3,90px);grid-auto-rows:104px;gap:7px 7px">
    <div class="tile blue" style="font-size:7.5px"><span class="ico" role="img" aria-label="Puzzle head icon" style="width:54px;height:54px"></span>TRAINING CENTER</div>
    <div class="tile violet" style="font-size:7.5px"><span class="ico" role="img" aria-label="Game controller icon" style="width:54px;height:54px"></span>GAMES LIST</div>
    <div class="tile violet" style="font-size:7.5px"><span class="ico" role="img" aria-label="Head with gears icon" style="width:54px;height:54px"></span>LEARNING</div>
    <div class="tile blue" style="font-size:7.5px"><span class="ico" role="img" aria-label="Brain icon" style="width:54px;height:54px"></span>ABOUT</div>
    <div class="tile blue" style="font-size:7.5px"><span class="ico" role="img" aria-label="Calendar icon" style="width:54px;height:54px"></span>SCHEDULE</div>
    <div class="tile violet" style="font-size:7.5px"><span class="ico" role="img" aria-label="Stars scoreboard icon" style="width:54px;height:54px"></span>SCORES</div>
  </div>
</section>

<!-- Landscape, Spanish -->
<section class="screen land" style="left:299px;top:2046px;width:603px;height:268px">
  <div class="bar" style="height:64px"><span class="dot info"></span>bienvenido Invitado<span class="dot"></span></div>
  <div class="lgrid" style="left:14px;right:14px;top:66px;grid-template-columns:repeat(6,1fr);grid-auto-rows:104px;gap:7px">
    <div class="tile blue" style="font-size:7.5px"><span class="ico" role="img" aria-label="Puzzle head icon" style="width:54px;height:54px"></span>CENTRO DE<br>ENTRENAMIENTO</div>
    <div class="tile violet" style="font-size:7.5px"><span class="ico" role="img" aria-label="Game controller icon" style="width:54px;height:54px"></span>LISTA DE<br>JUEGOS</div>
    <div class="tile blue" style="font-size:7.5px"><span class="ico" role="img" aria-label="Head with gears icon" style="width:54px;height:54px"></span>CONFIGURACIÓN</div>
    <div class="tile violet" style="font-size:7.5px"><span class="ico" role="img" aria-label="Brain icon" style="width:54px;height:54px"></span>MÁS<br>APLICACIONES</div>
    <div class="tile blue" style="font-size:7.5px"><span class="ico" role="img" aria-label="Calendar icon" style="width:54px;height:54px"></span>PROGRAMA</div>
    <div class="tile violet" style="font-size:7.5px"><span class="ico" role="img" aria-label="Upgrade arrow icon" style="width:54px;height:54px"></span>ACTUALIZAR</div>
  </div>
  <div class="wide" style="top:182px;height:76px;padding:0 16px 0 20px;gap:20px">
    <div style="flex:1"><h4>WATCH DEMO</h4>Sed ut perspiciatis unde omnis iste natus error sit voluptatem accusantium doloremque laudantium, totam rem aperiam, eaque ipsa</div><span class="btn" style="margin:0">LEARN MORE</span>
  </div>
</section>

</body>
</html>
```